Business Card Design Project

Build kick ass business card.
Updates

I just uploaded the Vorintex Logo in AI format, for those that were asking. It's looking real good and we'll be reviewing the designs soon. Thanks. 

Target Market(s)

Businesses in many verticals. Focusing on information security.

Vorintex, LLC
Gordon Bexley
Principal Security Consultant
Mobile: +1-602-555-0187
Email: Gordon.Bexley@Vorintex.example
Web: www.vorintex.example

Industry/Entity Type

Business

Requirements
Must have
• Design must look high-end, hi-tech stylish and minimalist

Be different – one that stands out from thousands of others

Does not have to be traditional rectangle

Would like logo integrated

```html
<!DOCTYPE html>
<html lang="en">
<head>
<meta charset="utf-8">
<title>Vorintex — Business Card</title>
<link rel="stylesheet" href="https://fonts.googleapis.com/css2?family=Open+Sans:wght@400;600&display=swap">
<style>
  :root {
    --backdrop: #d8d3cb;
    --card-frost: #eceeef;
    --card-edge: #ffffff;
    --band-white: #ffffff;
    --accent-blue: #1e9fd2;
    --block-blue: #4fb4d3;
    --ink-dark: #3a3a3a;
    --ink-mid: #444444;
    --mark-grey: #4a4f55;
  }
  * { margin: 0; padding: 0; box-sizing: border-box; }
  html, body {
    width: 1200px;
    height: 970px;
    overflow: hidden;
    background: var(--backdrop);
    font-family: "Open Sans", Arial, sans-serif;
  }
  .card {
    position: absolute;
    left: 100px;
    top: 208px;
    width: 1000px;
    height: 554px;
    background: linear-gradient(160deg, #f3f4f5 0%, var(--card-frost) 55%, #e3e6e8 100%);
    border: 2px solid var(--card-edge);
    border-radius: 6px;
    box-shadow: 0 10px 30px rgba(0,0,0,0.12);
  }
  .holder-name {
    position: absolute;
    left: 547px;
    top: 30px;
    font-size: 48px;
    font-weight: 400;
    color: var(--accent-blue);
    letter-spacing: 0.5px;
    white-space: nowrap;
  }
  .holder-title {
    position: absolute;
    left: 549px;
    top: 98px;
    font-size: 22px;
    color: var(--ink-mid);
    white-space: nowrap;
  }
  .brand-band {
    position: absolute;
    left: 0;
    top: 179px;
    width: 662px;
    height: 195px;
    background: var(--band-white);
    display: flex;
    align-items: center;
    padding-left: 120px;
    gap: 30px;
  }
  .brand-dot {
    width: 70px;
    height: 70px;
    border-radius: 50%;
    background: var(--accent-blue);
    flex: none;
  }
  .brand-name {
    font-size: 54px;
    font-weight: 400;
    color: var(--mark-grey);
    letter-spacing: 2px;
    text-transform: uppercase;
  }
  .accent-block {
    position: absolute;
    left: 906px;
    top: 179px;
    width: 92px;
    height: 195px;
    background: var(--block-blue);
  }
  .contact-list {
    position: absolute;
    left: 543px;
    right: 37px;
    top: 428px;
    font-size: 22px;
    color: var(--ink-dark);
  }
  .contact-row {
    display: flex;
    justify-content: space-between;
    line-height: 28px;
  }
</style>
</head>
<body>
  <div class="card">
    <div class="holder-name">Gordon Bexley</div>
    <div class="holder-title">Principal Security Consultant</div>

    <div class="brand-band">
      <span class="brand-dot"></span>
      <span class="brand-name">Vorintex</span>
    </div>

    <div class="accent-block"></div>

    <div class="contact-list">
      <div class="contact-row"><span class="contact-label">Mobile:</span><span class="contact-value">+1-602-555-0187</span></div>
      <div class="contact-row"><span class="contact-label">Email:</span><span class="contact-value">Gordon.Bexley@Vorintex.example</span></div>
      <div class="contact-row"><span class="contact-label">Web:</span><span class="contact-value">www.vorintex.example</span></div>
    </div>
  </div>
</body>
</html>
```